mothers day ad for martial arts school

I am looking to have a nice flyer/handout to promote my martial arts school. It is for our promotion of "mom's train free" for mothers day in May. I would like an ad that would inspire a mother to learn self defense and to improve their fitness. It can have pictures but not necessarily a requirement. Pictures don't have to be of a lady in a martial arts uniform. It may be better if they are not. It also doesn't have to be standard sheet of paper size, as these are going to be handouts the size can be smaller. I would like our Copper Vale logo on the flyer.

Target Market(s)

mothers that hadn't thought about martial arts before but would be convinced to try it

Industry/Entity Type

School

Requirements
Must have
• text, photos that would appeal to and encourage a mother to try a self defense/fitness class
Nice to have
• our logo and text and possibly pictures that would inspire a mother to join a martial arts class

```html
<!DOCTYPE html>
<html lang="en">
<head>
<meta charset="utf-8">
<title>Mom's Train Free – Copper Vale Martial Arts</title>
<link rel="stylesheet" href="https://fonts.googleapis.com/css2?family=Archivo+Black&family=Yellowtail&family=Roboto+Condensed:wght@700&family=Lilita+One&display=swap">
<style>
  :root {
    --ink: #0b0a09;
    --white: #ffffff;
    --red: #c4253a;
    --photo-warm: #6a4a35;
    --photo-mid: #2a1d16;
    --panel: rgba(0, 0, 0, 0.55);
  }
  html, body {
    margin: 0;
    padding: 0;
    overflow: hidden;
    background: var(--ink);
  }
  .flyer {
    position: relative;
    width: 906px;
    height: 1200px;
    overflow: hidden;
    background: var(--ink);
  }
  .flyer h1, .flyer p { margin: 0; }
  .hero-photo {
    position: absolute;
    inset: 0;
    background:
      radial-gradient(ellipse 300px 380px at 470px 430px, var(--photo-warm) 0%, var(--photo-mid) 55%, transparent 100%),
      radial-gradient(ellipse 260px 320px at 160px 680px, #7a5a44 0%, transparent 80%),
      var(--ink);
  }
  .brand {
    position: absolute;
    left: 50px;
    top: 18px;
    width: 416px;
    height: 100px;
    background: var(--white);
    display: flex;
    align-items: center;
    justify-content: center;
    gap: 12px;
  }
  .brand-mark {
    width: 30px;
    height: 30px;
    background: var(--red);
    flex: none;
  }
  .brand-name {
    font-family: "Lilita One", sans-serif;
    font-size: 31px;
    color: var(--ink);
    white-space: nowrap;
  }
  .frame {
    position: absolute;
    left: 0;
    top: 0;
  }
  .headline-script {
    position: absolute;
    left: 0;
    width: 906px;
    top: 305px;
    text-align: center;
    font-family: "Yellowtail", cursive;
    font-weight: 400;
    font-size: 98px;
    line-height: 110px;
    color: var(--white);
    text-shadow: 3px 3px 0 var(--ink);
    white-space: nowrap;
  }
  .offer-panel {
    position: absolute;
    left: 98px;
    top: 790px;
    width: 730px;
    height: 266px;
    background: var(--panel);
  }
  .invite {
    position: absolute;
    left: 0;
    width: 906px;
    top: 796px;
    text-align: center;
    font-family: "Yellowtail", cursive;
    font-size: 86px;
    line-height: 100px;
    color: var(--red);
    text-shadow: 2px 2px 0 var(--white);
    white-space: nowrap;
  }
  .offer-details {
    position: absolute;
    left: 0;
    width: 906px;
    top: 914px;
    text-align: center;
    font-family: "Roboto Condensed", sans-serif;
    font-weight: 700;
    font-size: 60px;
    line-height: 62px;
    color: var(--white);
    white-space: nowrap;
  }
  .taglines {
    position: absolute;
    left: 0;
    width: 906px;
    top: 1136px;
    text-align: center;
    font-family: "Lilita One", sans-serif;
    font-size: 40px;
    line-height: 48px;
    color: var(--white);
    white-space: nowrap;
  }
  .taglines .dot { margin: 0 14px; }
</style>
</head>
<body>
<main class="flyer">
  <div class="hero-photo" role="img" aria-label="Photo of a determined woman in a fighting stance throwing a punch toward the viewer, on a dark background"></div>

  <svg class="frame" width="906" height="1200" viewBox="0 0 906 1200" aria-hidden="true">
    <g fill="var(--red)">
      <rect x="51" y="138" width="810" height="18"/>
      <rect x="51" y="1080" width="810" height="18"/>
      <rect x="51" y="138" width="19" height="368"/>
      <rect x="51" y="730" width="19" height="368"/>
      <rect x="842" y="138" width="19" height="368"/>
      <rect x="842" y="730" width="19" height="368"/>
    </g>
    <text x="468" y="738" text-anchor="middle" textLength="676" lengthAdjust="spacingAndGlyphs"
          font-family="Archivo Black, sans-serif" font-size="350" fill="var(--ink)">FREE</text>
    <text x="462" y="732" text-anchor="middle" textLength="676" lengthAdjust="spacingAndGlyphs"
          font-family="Archivo Black, sans-serif" font-size="350" fill="var(--white)">FREE</text>
  </svg>

  <header class="brand">
    <span class="brand-mark"></span>
    <span class="brand-name">Copper Vale Martial Arts</span>
  </header>

  <h1 class="headline-script">Mom’s Train</h1>

  <div class="offer-panel"></div>
  <p class="invite">Come Join Us!</p>
  <p class="offer-details">Train Free For 30 Days When<br>You Start On May 31st</p>

  <p class="taglines">Feel Strong<span class="dot">•</span>Look Good<span class="dot">•</span>Get Strong<span class="dot">•</span>Feel Safe</p>
</main>
</body>
</html>
```